Orbell Consulting- executive coaching business

looking for business card design for a newly started coaching business.
specialising in Exective coaching, Leadership, NLP and Motivation.
Looking for a simple, classy design using the existing logo attached and colour themes that complement the logo.
No red or orange in the business card design please.

Target Market(s)

Defence and Veteran community

Industry/Entity Type

Life Coaching

Contact Information for Business Card

looking for business cards for newly started coaching business.
specialising in Exective Coaching, Leadership, NLP and Motivation

Font styles to use
Serif
Script

Colors
0556a4
3176b5
86cfc6
33b8a4

Requirements
Must have
• Logo
• Email address- Jess@orbellconsulting.com.au
• Contact number
• Services provided - Executive Coaching, Leadership, NLP and Motivational Mapping.
Nice to have
• Same colours as logo
Should not have
• Red or orange

```html
<!DOCTYPE html>
<html lang="en">
<head>
<meta charset="utf-8">
<title>Orbell Consulting – Business Card</title>
<link href="https://fonts.googleapis.com/css2?family=Roboto:wght@400;500;700&display=swap" rel="stylesheet">
<style>
  :root {
    --stage: #3a302c;
    --card: #fbfbfc;
    --brand-blue: #2c5ba8;
    --accent-green: #2c9f58;
    --divider-grey: #8b8b8d;
    --ink: #4a4a4c;
    --ink-soft: #77777a;
    --on-blue: #ffffff;
  }
  * { margin: 0; padding: 0; box-sizing: border-box; }
  html, body {
    width: 1200px; height: 716px; overflow: hidden;
    background: var(--stage);
    font-family: "Roboto", Arial, sans-serif;
  }
  .business-card {
    position: absolute; left: 120px; top: 84px;
    width: 960px; height: 549px;
    background: var(--card);
    overflow: hidden;
    box-shadow: 0 10px 30px rgba(0,0,0,.35);
  }
  .card-waves { position: absolute; inset: 0; }
  .services {
    position: absolute; right: 40px; top: 130px;
    list-style: none; text-align: right;
    color: var(--on-blue); font-size: 21px; line-height: 31px;
  }
  .services li::after { content: " «"; }
  .brand {
    position: absolute; left: 80px; top: 120px; width: 380px;
    text-align: center;
  }
  .brand-dot {
    display: block; margin: 0 auto 14px;
    width: 76px; height: 76px; border-radius: 50%;
    border: 3px solid var(--divider-grey);
  }
  .brand-name {
    color: var(--brand-blue); font-weight: 500;
    font-size: 35px; letter-spacing: .5px; white-space: nowrap;
  }
  .contact {
    position: absolute; left: 80px; top: 300px;
    list-style: none; color: var(--ink); font-size: 20px;
  }
  .contact li { display: flex; align-items: center; height: 32px; }
  .contact svg { width: 20px; height: 20px; margin-right: 16px; fill: var(--brand-blue); }
  .person { position: absolute; left: 700px; top: 440px; }
  .person-name { color: var(--brand-blue); font-weight: 700; font-size: 32px; }
  .person-title { color: var(--ink-soft); font-size: 18px; margin-top: 4px; }
</style>
</head>
<body>
  <div class="business-card">
    <svg class="card-waves" viewBox="0 0 960 549" aria-hidden="true">
      <path d="M0,0 H960 V330 C820,312 650,250 570,160 C490,72 300,28 0,18 Z" fill="var(--brand-blue)"/>
      <path d="M0,32 C280,40 440,70 530,128" fill="none" stroke="var(--accent-green)" stroke-width="9"/>
      <path d="M0,40 C260,48 420,82 520,140" fill="none" stroke="var(--card)" stroke-width="6"/>
      <path d="M575,185 C660,285 810,336 960,352" fill="none" stroke="var(--divider-grey)" stroke-width="9"/>
    </svg>

    <ul class="services">
      <li>NLP &amp; Motivational Mapping</li>
      <li>Executive Coaching</li>
      <li>Leadership</li>
    </ul>

    <div class="brand">
      <span class="brand-dot"></span>
      <div class="brand-name">ORBELL CONSULTING</div>
    </div>

    <ul class="contact">
      <li>
        <svg viewBox="0 0 24 24"><path d="M6.6 10.8a15.1 15.1 0 0 0 6.6 6.6l2.2-2.2a1 1 0 0 1 1-.25 11.4 11.4 0 0 0 3.6.57 1 1 0 0 1 1 1V20a1 1 0 0 1-1 1A17 17 0 0 1 3 4a1 1 0 0 1 1-1h3.5a1 1 0 0 1 1 1c0 1.25.2 2.45.57 3.57a1 1 0 0 1-.25 1z"/></svg>
        +00 123 456 7890
      </li>
      <li>
        <svg viewBox="0 0 24 24"><path d="M2 5h20v14H2z M2 5l10 8 10-8" fill="none" stroke="var(--brand-blue)" stroke-width="2"/></svg>
        Jess@orbellconsulting.com.au
      </li>
      <li>
        <svg viewBox="0 0 24 24"><circle cx="12" cy="12" r="9" fill="none" stroke="var(--brand-blue)" stroke-width="2"/><path d="M3 12h18M12 3c3 3 3 15 0 18M12 3c-3 3-3 15 0 18" fill="none" stroke="var(--brand-blue)" stroke-width="1.6"/></svg>
        www.orbellconsulting.com.au
      </li>
    </ul>

    <div class="person">
      <div class="person-name">Jess Harlow</div>
      <div class="person-title">Managing Director</div>
    </div>
  </div>
</body>
</html>
```